Custom Clothing Store Website/Logo Design

We need a website and Logo design for our company called "quillbarn7823". We will be designing generic and mainly custom made clothing (t shirts, sweaters, hoodies, hats, caps, leggings etc) with other products of electronics and every day products with side sells. We want a catchy but easy to navigate website to use on our SHOPIFY website.
Updates

Designs look the same

Target Market(s)

Anyone that is interested in purchasing custom design clothing.

Logo Text

QuillBarn23'

Number of Pages Required

1 page

Other font styles liked:
• Microbrew

Colors

Designer to choose colors to be used in the design.

```html
<!DOCTYPE html>
<html lang="en">
<head>
<meta charset="utf-8">
<title>QuillBarn7823 — Custom clothing store</title>
<link rel="stylesheet" href="https://fonts.googleapis.com/css2?family=Montserrat:wght@400;500;600;700&family=Open+Sans:wght@400;600;700&display=swap">
<style>
:root{
  --accent:#1fb4d8;
  --accent-dark:#1397b8;
  --ink:#1c1c1c;
  --text:#555;
  --muted:#777;
  --white:#fff;
  --grey-bg:#f2f2f2;
  --card-border:#dedede;
  --news-bg:#d8e9ee;
  --footer-bg:#f4f4f4;
}
*{box-sizing:border-box;margin:0;padding:0}
html,body{width:1200px;height:4762px;overflow:hidden}
body{position:relative;background:var(--white);font-family:"Open Sans",Arial,sans-serif;color:var(--text)}
section,header,footer{position:absolute;left:0;width:1200px}
.abs{position:absolute}
.section-title{position:absolute;left:0;width:1200px;text-align:center;font-family:"Montserrat",Arial,sans-serif;font-weight:400;font-size:40px;letter-spacing:1px;color:var(--ink);text-transform:uppercase}
.section-title b{font-weight:700}

/* hero */
.hero{top:0;height:645px;overflow:hidden}
.hero-photo{position:absolute;inset:0;background:
  radial-gradient(ellipse at 80% 70%,#e0603c 0%,rgba(224,96,60,0) 45%),
  radial-gradient(ellipse at 20% 40%,#b9473a 0%,rgba(185,71,58,0) 40%),
  linear-gradient(120deg,#6b5a4e 0%,#c9b9a9 35%,#e9e1d8 55%,#d98b6c 80%,#c5c0bb 100%)}
.hero-shade{position:absolute;inset:0;background:rgba(20,20,20,.28)}
.brand{position:absolute;left:111px;top:62px;font-family:"Montserrat",Arial,sans-serif;font-weight:700;font-size:25px;color:var(--white);letter-spacing:.5px}
.main-nav{position:absolute;left:450px;top:68px;display:flex;gap:30px}
.main-nav a{font-family:"Montserrat",Arial,sans-serif;font-size:14px;font-weight:500;color:var(--white);text-decoration:none;letter-spacing:.5px}
.nav-icons{position:absolute;left:924px;top:50px;display:flex;gap:14px}
.nav-icon{width:46px;height:46px;border-radius:50%;border:2px solid var(--white);display:flex;align-items:center;justify-content:center}
.nav-icon.cart{background:var(--accent);border-color:var(--accent)}
.hero-title{position:absolute;top:205px;left:0;width:1200px;text-align:center;font-family:"Montserrat",Arial,sans-serif;font-weight:700;font-size:76px;color:var(--white);letter-spacing:2px}
.hero-sub{position:absolute;top:307px;left:0;width:1200px;text-align:center;font-family:"Open Sans",Arial,sans-serif;font-size:34px;color:var(--white)}
.btn-outline-light{position:absolute;left:503px;top:393px;width:194px;height:52px;border:2px solid var(--white);border-radius:26px;color:var(--white);font-family:"Montserrat",Arial,sans-serif;font-weight:700;font-size:15px;display:flex;align-items:center;justify-content:center;letter-spacing:1px}
.hero-dots{position:absolute;top:564px;left:569px;display:flex;gap:6px}
.hero-dots span{width:13px;height:13px;border-radius:50%;border:2px solid var(--white)}
.hero-dots span.on{background:var(--white)}

/* welcome */
.welcome{top:645px;height:387px;background:var(--white)}
.welcome .section-title{top:92px}
.welcome-text{position:absolute;left:170px;top:168px;width:860px;text-align:center;font-size:13px;line-height:28px;color:var(--muted)}

/* products */
.featured{top:1032px;height:1705px;background:var(--grey-bg)}
.featured .section-title{top:125px}
.product{position:absolute}
.product-card{position:absolute;left:0;top:0;background:var(--white);border:1px solid var(--card-border);box-shadow:0 1px 3px rgba(0,0,0,.06)}
.product-photo{position:absolute;left:15%;top:12%;width:70%;height:76%;border-radius:10px}
.product-name{position:absolute;left:0;width:100%;text-align:center;font-size:22px;color:#333}
.btn-solid{position:absolute;background:var(--accent);color:var(--white);border-radius:35px;font-family:"Montserrat",Arial,sans-serif;font-weight:700;font-size:15px;display:flex;align-items:center;justify-content:center;letter-spacing:1px}

/* newsletter */
.newsletter{top:2737px;height:390px;background:var(--news-bg)}
.newsletter .section-title{top:100px}
.news-sub{position:absolute;top:170px;left:0;width:1200px;text-align:center;font-size:17px;color:#444}
.news-input{position:absolute;left:302px;top:238px;width:450px;height:57px;background:var(--white);font-size:15px;color:#555;padding-left:28px;display:flex;align-items:center}
.news-btn{position:absolute;left:752px;top:238px;width:146px;height:57px;background:var(--accent);color:var(--white);font-family:"Montserrat",Arial,sans-serif;font-weight:700;font-size:14px;display:flex;align-items:center;justify-content:center;letter-spacing:.5px}

/* blog */
.blog{top:3127px;height:1207px;background:var(--white)}
.blog .section-title{top:118px}
.post-title{position:absolute;width:460px;font-family:"Open Sans",Arial,sans-serif;font-weight:600;font-size:24px;line-height:33px;color:var(--ink)}
.post-meta{position:absolute;font-size:13px;color:#444;display:flex;align-items:center;gap:8px}
.post-body{position:absolute;width:450px;font-size:13px;line-height:26px;color:var(--muted)}
.btn-read{position:absolute;width:130px;height:44px;border:2px solid var(--accent);border-radius:22px;color:var(--accent-dark);font-family:"Montserrat",Arial,sans-serif;font-weight:700;font-size:13px;display:flex;align-items:center;justify-content:center;letter-spacing:.5px}
.post-photo-frame{position:absolute;box-shadow:10px 10px 0 var(--accent)}
.post-photo{width:100%;height:100%}

/* footer */
.site-footer{top:4334px;height:428px;background:var(--footer-bg)}
.footer-col{position:absolute;top:92px}
.footer-col h4{font-family:"Montserrat",Arial,sans-serif;font-weight:700;font-size:17px;color:var(--ink);letter-spacing:.5px;margin-bottom:16px}
.footer-col ul{list-style:none}
.footer-col li{font-size:13px;line-height:27px;color:#555}
.social li{display:flex;align-items:center;gap:14px;line-height:42px}
.social-dot{width:28px;height:28px;border-radius:50%;border:2px solid var(--accent)}
.about-text{width:300px;font-size:13px;line-height:22px;color:#555}
.footer-rule{position:absolute;left:111px;top:333px;width:978px;height:1px;background:#dcdcdc}
.copyright{position:absolute;left:111px;top:362px;font-size:13px;color:#555}
.pay-badges{position:absolute;left:852px;top:356px;display:flex;gap:6px}
.pay-badges span{width:42px;height:24px;border-radius:3px;background:#b5b5b5}
</style>
</head>
<body>

<header class="hero">
  <div class="hero-photo" role="img" aria-label="Close-up of colourful garments hanging on a clothing rail"></div>
  <div class="hero-shade"></div>
  <div class="brand">QUILLBARN7823</div>
  <nav class="main-nav">
    <a href="#">CLOTHING</a><a href="#">ELECTRONICS</a><a href="#">OTHER</a><a href="#">CONTACT</a>
  </nav>
  <div class="nav-icons">
    <div class="nav-icon"><svg width="20" height="20" viewBox="0 0 20 20"><circle cx="8" cy="8" r="6" fill="none" stroke="#fff" stroke-width="2.2"/><line x1="12.5" y1="12.5" x2="18" y2="18" stroke="#fff" stroke-width="2.4" stroke-linecap="round"/></svg></div>
    <div class="nav-icon"><svg width="18" height="20" viewBox="0 0 18 20"><circle cx="9" cy="6" r="4.5" fill="#fff"/><path d="M1 19c0-5 3.6-7.5 8-7.5s8 2.5 8 7.5z" fill="#fff"/></svg></div>
    <div class="nav-icon cart"><svg width="20" height="20" viewBox="0 0 20 20"><path d="M1 2h3l2.5 10h10l2-7H6" fill="none" stroke="#fff" stroke-width="2" stroke-linejoin="round"/><circle cx="8" cy="16.5" r="1.8" fill="#fff"/><circle cx="15" cy="16.5" r="1.8" fill="#fff"/></svg></div>
  </div>
  <h1 class="hero-title">QUILLBARN7823</h1>
  <p class="hero-sub">Custom clothing store</p>
  <div class="btn-outline-light">SHOP NOW!</div>
  <div class="hero-dots"><span class="on"></span><span></span><span></span><span></span></div>
</header>

<section class="welcome">
  <h2 class="section-title">Welcome to <b>QuillBarn7823</b></h2>
  <p class="welcome-text">Nam libero tempore, cum soluta nobis est eligendi optio cumque nihil impedit quo minus id quod maxime placeat facere possimus, omnis voluptas assumenda est, omnis dolor repellendus. Temporibus autem quibusdam et aut officiis debitis aut rerum necessitatibus saepe eveniet ut et voluptates repudiandae sint et molestiae non recusandae. Itaque earum rerum hic tenetur a sapiente delectus, ut aut reiciendis voluptatibus maiores alias consequatur aut perferendis doloribus asperiores.</p>
</section>

<section class="featured">
  <h2 class="section-title">Featured <b>Products</b></h2>

  <div class="product" style="left:111px;top:238px;width:572px;height:565px">
    <div class="product-card" style="width:572px;height:483px"><div class="product-photo" role="img" aria-label="Black t-shirt" style="background:radial-gradient(ellipse at center,#1a1a1a 0%,#2a2a2a 50%,rgba(255,255,255,0) 72%)"></div></div>
    <div class="product-name" style="top:500px">T shirts</div>
  </div>
  <div class="product" style="left:714px;top:238px;width:372px;height:280px">
    <div class="product-card" style="width:372px;height:200px"><div class="product-photo" role="img" aria-label="Stack of folded grey sweaters" style="background:radial-gradient(ellipse at center,#8d8d8d 0%,#b0b0b0 45%,rgba(255,255,255,0) 72%)"></div></div>
    <div class="product-name" style="top:224px">Sweaters</div>
  </div>
  <div class="product" style="left:714px;top:521px;width:372px;height:280px">
    <div class="product-card" style="width:372px;height:200px"><div class="product-photo" role="img" aria-label="Grey hoodie" style="background:radial-gradient(ellipse at center,#6f6f6f 0%,#929292 45%,rgba(255,255,255,0) 72%)"></div></div>
    <div class="product-name" style="top:212px">Hoodies</div>
  </div>

  <div class="product" style="left:111px;top:873px;width:372px;height:280px">
    <div class="product-card" style="width:372px;height:197px"><div class="product-photo" role="img" aria-label="Olive bucket hat" style="background:radial-gradient(ellipse at center,#7b6a30 0%,#9a8a4a 45%,rgba(255,255,255,0) 72%)"></div></div>
    <div class="product-name" style="top:227px">Hats</div>
  </div>
  <div class="product" style="left:111px;top:1159px;width:372px;height:280px">
    <div class="product-card" style="width:372px;height:197px"><div class="product-photo" role="img" aria-label="Black baseball cap" style="background:radial-gradient(ellipse at center,#151515 0%,#2c2c2c 45%,rgba(255,255,255,0) 72%)"></div></div>
    <div class="product-name" style="top:227px">Caps</div>
  </div>
  <div class="product" style="left:514px;top:873px;width:572px;height:565px">
    <div class="product-card" style="width:572px;height:483px"><div class="product-photo" role="img" aria-label="Patterned and black leggings laid flat" style="background:linear-gradient(90deg,rgba(255,255,255,0) 0%,#bdbdbd 20%,#9a9a9a 45%,#222 60%,#2b2b2b 80%,rgba(255,255,255,0) 100%)"></div></div>
    <div class="product-name" style="top:513px">Leggings</div>
  </div>

  <div class="btn-solid" style="left:505px;top:1498px;width:190px;height:70px">VIEW MORE</div>
</section>

<section class="newsletter">
  <h2 class="section-title">Subscribe to <b>our newsletter</b></h2>
  <p class="news-sub">Sign up to stay in the loop. Receive updates, access to exclusive deals, and more</p>
  <div class="news-input">Email Address</div>
  <div class="news-btn">SUBSCRIBE</div>
</section>

<section class="blog">
  <h2 class="section-title">From the <b>Blog</b></h2>

  <article>
    <h3 class="post-title" style="left:111px;top:277px">Sed ut perspiciatis unde omnis istnatus sivol uptatem accusantium dolo</h3>
    <div class="post-meta" style="left:111px;top:366px">
      <svg width="13" height="13" viewBox="0 0 13 13"><rect x="1" y="2" width="11" height="10" rx="1" fill="none" stroke="#1fb4d8" stroke-width="1.5"/><line x1="1" y1="5" x2="12" y2="5" stroke="#1fb4d8" stroke-width="1.5"/></svg>
      <span>10/09/2018</span><span>|</span>
      <svg width="12" height="13" viewBox="0 0 12 13"><circle cx="6" cy="4" r="3" fill="#1fb4d8"/><path d="M0 13c0-4 2.7-5.5 6-5.5s6 1.5 6 5.5z" fill="#1fb4d8"/></svg>
      <span>John Doe</span>
    </div>
    <p class="post-body" style="left:111px;top:400px">Nemo enim ipsam voluptatem quia voluptas sit aspernatur aut odit aut fugit, sed quia consequuntur magni dolores eos qui ratione voluptatem sequi nesciunt. Neque porro quisquam est, qui dolorem ipsum quia dolor sit amet, consectetur, adipisci velit, sed quia.</p>
    <div class="btn-read" style="left:111px;top:537px">READ MORE</div>
    <div class="post-photo-frame" style="left:613px;top:254px;width:463px;height:350px">
      <div class="post-photo" role="img" aria-label="Tailoring studio with a dress form and a rack of garments" style="background:linear-gradient(110deg,#ece8e3 0%,#d9d2ca 40%,#8a7f78 60%,#4b4747 80%,#d7cfc6 100%)"></div>
    </div>
  </article>

  <article>
    <div class="post-photo-frame" style="left:111px;top:715px;width:466px;height:355px">
      <div class="post-photo" role="img" aria-label="Person with headphones looking at a phone" style="background:linear-gradient(135deg,#3a4d4e 0%,#6e8383 45%,#2f3b3c 100%)"></div>
    </div>
    <h3 class="post-title" style="left:648px;top:740px">Sed ut perspiciatis unde omnis istnatus sivol uptatem accusantium dolo</h3>
    <div class="post-meta" style="left:648px;top:828px">
      <svg width="13" height="13" viewBox="0 0 13 13"><rect x="1" y="2" width="11" height="10" rx="1" fill="none" stroke="#1fb4d8" stroke-width="1.5"/><line x1="1" y1="5" x2="12" y2="5" stroke="#1fb4d8" stroke-width="1.5"/></svg>
      <span>10/09/2018</span><span>|</span>
      <svg width="12" height="13" viewBox="0 0 12 13"><circle cx="6" cy="4" r="3" fill="#1fb4d8"/><path d="M0 13c0-4 2.7-5.5 6-5.5s6 1.5 6 5.5z" fill="#1fb4d8"/></svg>
      <span>John Doe</span>
    </div>
    <p class="post-body" style="left:648px;top:862px">Nemo enim ipsam voluptatem quia voluptas sit aspernatur aut odit aut fugit, sed quia consequuntur magni dolores eos qui ratione voluptatem sequi nesciunt. Neque porro quisquam est, qui dolorem ipsum quia dolor sit amet, consectetur, adipisci velit, sed quia.</p>
    <div class="btn-read" style="left:648px;top:1000px">READ MORE</div>
  </article>
</section>

<footer class="site-footer">
  <div class="footer-col" style="left:111px">
    <h4>INFORMATION</h4>
    <ul><li>About Us</li><li>Careers</li><li>Privacy &amp; Security</li><li>Site Map</li><li>Terms of Use</li><li>Blog</li></ul>
  </div>
  <div class="footer-col" style="left:314px">
    <h4>HELP &amp; SUPPORT</h4>
    <ul><li>Recommended Reading</li><li>Submit your Story</li><li>Contact Us</li><li>FAQ</li><li>How to Order</li></ul>
  </div>
  <div class="footer-col social" style="left:549px">
    <h4>STAY CONNECTED</h4>
    <ul><li><span class="social-dot"></span>Facelane</li><li><span class="social-dot"></span>Snapgram</li><li><span class="social-dot"></span>Email</li><li><span class="social-dot"></span>Linkwork</li></ul>
  </div>
  <div class="footer-col" style="left:790px">
    <h4>ABOUT</h4>
    <p class="about-text">At vero eos et accusamus et iusto odio dignissimos ducimus qui blanditiis praesentium voluptatum deleniti atque corrupti quos dolores quas molestias excepturi sint occaecati cupiditate non provident, similique sunt in culpa.</p>
  </div>
  <div class="footer-rule"></div>
  <p class="copyright">Copyrights © 2019, QuillBarn7823. All Rights Reserved.</p>
  <div class="pay-badges"><span></span><span></span><span></span><span></span><span></span></div>
</footer>

</body>
</html>
```